Corporate flyer introducing a brand new technology apprenticeship program in Australia!

A professional, yet clean and contemporary looking flyer to advertise a brand new service offering in a simple, easy to read format with engaging images. Here is a link to our current online brochure which outlines the program we would like to advertise in a hardcopy flyer/brochure format: https://pages.vendrap.com/Information-on-Technology-Higher-Apprenticeships-for-Employers-Victoria-kT3pzqW7LmRe

Target Market(s)

Medium to large sized businesses involved in using cutting edge technology, such as engineering and advanced manufracturing (3D printing etc)

Industry/Entity Type

Engineering

Colors

Designer to choose colors to be used in the design.

Requirements
Must have
• Contemporary, clean looking, easy to read, tech/engineering/advanced manufacturing related imagery
Nice to have
• Some ideas about different sizes/styles (eg something other than a plain A4 sheet)
Should not have
• Unprofessional or offensive language

```html
<!DOCTYPE html>
<html lang="en">
<head>
<meta charset="utf-8">
<title>Technology Higher Apprentices Flyer</title>
<link href="https://fonts.googleapis.com/css2?family=Montserrat:wght@400;500;600;700&family=Questrial&display=swap" rel="stylesheet">
<style>
:root{
  --orange:#e8501f;
  --blue:#1d6fb0;
  --blue-dark:#0f4f8a;
  --blue-light:#2a8fd6;
  --navy:#1a3f7a;
  --grey-panel:#e4e4e4;
  --grey-band:#e6e6e6;
  --ink:#333;
  --stage:#ebebeb;
}
*{margin:0;padding:0;box-sizing:border-box}
html,body{width:1200px;height:861px;overflow:hidden}
body{background:var(--stage);position:relative;font-family:"Questrial",sans-serif;color:var(--ink)}
.flyer{position:absolute;top:160px;width:410px;height:580px;background:#fff;overflow:hidden;box-shadow:0 4px 14px rgba(0,0,0,.18)}
.flyer--intro{left:174px}
.flyer--structure{left:636px}
.abs{position:absolute}
.brand-band{background:var(--orange);color:#fff;display:flex;align-items:center;font-family:"Montserrat",sans-serif;font-weight:600;letter-spacing:.5px}
.brand-band .mark{width:9px;height:9px;background:#fff;margin-right:7px;flex:none}
.intro-brand{left:0;top:12px;width:200px;height:72px;padding-left:16px;font-size:15px;clip-path:polygon(0 0,100% 0,86% 100%,0 100%)}
.structure-brand{left:0;top:16px;width:152px;height:50px;padding-left:12px;font-size:12px;clip-path:polygon(0 0,100% 0,84% 100%,0 100%)}
.photo{background:linear-gradient(160deg,#c9d8e8 0%,#8ea6bf 45%,#5a6b7c 75%,#b89a73 100%)}
.intro-photo{left:168px;top:0;width:242px;height:200px;clip-path:polygon(26% 0,100% 0,100% 100%,0 100%)}
.title-panel{left:0;top:84px;width:196px;height:100px;background:var(--grey-panel);clip-path:polygon(0 0,100% 0,85% 100%,0 100%);padding:26px 0 0 13px;font-family:"Montserrat",sans-serif;color:#444}
.title-panel .kicker{font-size:11.5px;letter-spacing:.3px}
.title-panel .big{font-size:31px;font-weight:700;color:var(--navy);line-height:.95}
.title-panel .sub{font-size:17px;letter-spacing:.2px}
.pill{background:linear-gradient(180deg,var(--blue-light),var(--blue-dark));color:#fff;border-radius:14px;font-family:"Montserrat",sans-serif;font-weight:600;font-size:9px;display:flex;align-items:center;justify-content:center;box-shadow:0 2px 3px rgba(0,0,0,.25)}
.intro-pill{left:83px;top:214px;width:242px;height:27px}
.structure-pill{left:126px;top:152px;width:162px;height:27px}
.copy{font-size:5.6px;line-height:1.45}
.copy p{margin-bottom:4px}
.copy--center{text-align:center}
.copy--justify{text-align:justify}
.intro-copy{left:30px;top:252px;width:350px}
.pilot-heading{left:24px;top:355px;font-family:"Montserrat",sans-serif;font-size:14.5px;line-height:1.35;color:#222}
.pilot-heading strong{color:var(--blue);font-weight:600}
.illustration{left:200px;top:350px;width:184px;height:72px;border-radius:10px;background:linear-gradient(180deg,#cfe6f5,#a9d2ee);box-shadow:0 1px 3px rgba(0,0,0,.2)}
.col-left{left:24px;top:430px;width:166px}
.col-right{left:219px;top:436px;width:166px}
.footer-phone{left:0;top:550px;width:150px;height:30px;background:var(--blue);clip-path:polygon(0 0,100% 0,92% 100%,0 100%);color:#fff;font-family:"Montserrat",sans-serif;font-weight:600;font-size:11px;display:flex;align-items:center;padding-left:26px;gap:5px}
.footer-mail{left:146px;top:558px;width:264px;height:22px;background:var(--orange);clip-path:polygon(6% 0,100% 0,100% 100%,0 100%);color:#fff;font-size:8px;display:flex;align-items:center;justify-content:flex-end;padding-right:24px}
.structure-photo{left:0;top:0;width:410px;height:164px;background:linear-gradient(180deg,#7d8b96 0%,#4f5a63 55%,#2f363c 100%)}
.structure-copy{left:33px;top:189px;width:344px}
.units-title{left:0;top:252px;width:410px;text-align:center;font-family:"Montserrat",sans-serif;font-size:12px;color:#222}
.units-level{left:0;top:267px;width:410px;text-align:center;font-family:"Montserrat",sans-serif;font-weight:600;font-size:7px;color:var(--blue)}
.unit-list{list-style:none;font-family:"Montserrat",sans-serif;font-weight:600;font-size:5.6px;line-height:1.45;color:#333}
.unit-list li{position:relative;padding-left:9px;margin-bottom:5px}
.unit-list li::before{content:"";position:absolute;left:0;top:2.5px;width:3px;height:3px;border-radius:50%;background:var(--blue)}
.units-col1{left:14px;top:290px;width:92px}
.units-col2{left:108px;top:290px;width:116px}
.industry-visual{left:228px;top:289px;width:170px;height:135px;border-radius:8px;background:linear-gradient(135deg,#8a2a14,#d9541f 40%,#6b6b6b 75%,#b5b5b5);box-shadow:0 1px 4px rgba(0,0,0,.3)}
.advanced-band{left:0;top:452px;width:410px;height:98px;background:var(--grey-band)}
.advanced-level{left:14px;top:467px;font-family:"Montserrat",sans-serif;font-weight:600;font-size:7px;color:var(--blue)}
.advanced-rows{left:14px;top:482px;width:390px;font-family:"Montserrat",sans-serif;font-weight:600;font-size:5.6px;color:#333}
.advanced-rows .row{display:flex;gap:10px;height:12.6px;align-items:center}
.advanced-rows span{position:relative;padding-left:8px}
.advanced-rows span::before{content:"";position:absolute;left:0;top:2px;width:3px;height:3px;border-radius:50%;background:var(--blue)}
</style>
</head>
<body>

<section class="flyer flyer--intro">
  <div class="abs photo intro-photo" role="img" aria-label="Photo of a hand touching a screen of technology sketches over a city skyline"></div>
  <div class="abs brand-band intro-brand"><span class="mark"></span>Vantis Group</div>
  <div class="abs title-panel">
    <div class="kicker">TECHNOLOGY</div>
    <div class="big">HIGHER</div>
    <div class="sub">APPRENTICES</div>
  </div>
  <div class="abs pill intro-pill">TECHNOLOGY HIGHER APPRENTICES PROGRAM</div>
  <div class="abs copy copy--center intro-copy">
    <p>Join industry leaders in this unique program aimed at future proofing Australian businesses.</p>
    <p>The Technology Higher Apprenticeships combine the best of Higher Education and Vocational learning models by training future technicians to a higher skill and knowledge level to meet the needs of an Industry 4.0 based economy.</p>
    <p>These Higher Apprentices are employed in a model similar to a traditional paid apprenticeship while they are also enrolled in a Diploma of Applied Technologies, followed by an Associate Degree covering a range of topics related to emerging technology. The Higher Apprentices will also complete a number of intensive projects where they will commission a cyber-physical system to provide a solution or enhancement for your business. During these projects, the Higher Apprentices will have access to Eastbrook's world-class Factory of the Future.</p>
  </div>
  <h2 class="abs pilot-heading">Industry <strong>4.0 Higher</strong><br>Apprenticeships<br>Pilot Program</h2>
  <div class="abs illustration" role="img" aria-label="Illustration of the four industrial revolutions from steam machines to connected smart factories"></div>
  <div class="abs copy copy--justify col-left">
    <p>The program utilises an apprenticeship framework to deliver a new Diploma and Associate Degree in Applied Technologies.</p>
    <p>The original project is funded as a pilot by the Australian Government, led and managed by the Vantis Group, and implemented in collaboration with Kessler Systems and Eastbrook University of Technology.</p>
    <p>Focusing on Industry 4.0 and the Internet of Things, IT Disruptive Technologies, Engineering, Design and Business, the course will enable employers to train future technicians with a higher skills level to meet their needs in an Industry 4.0 based economy.</p>
  </div>
  <div class="abs copy copy--justify col-right">
    <p>The pilot combines the best of university and vocational learning models to improve Science, Technology, Engineering and Math (STEM) skills of technically minded participants, incorporating skills for business and design.</p>
    <p>The hands on and worked based component ensures applicants are productive in industry whilst applying the advanced knowledge gained from the off-the-job training.</p>
  </div>
  <div class="abs footer-phone">
    <svg width="10" height="10" viewBox="0 0 24 24" aria-hidden="true"><path fill="#fff" d="M6.6 10.8a15 15 0 0 0 6.6 6.6l2.2-2.2c.3-.3.7-.4 1-.2 1.1.4 2.3.6 3.6.6.6 0 1 .4 1 1V20c0 .6-.4 1-1 1A17 17 0 0 1 3 4c0-.6.4-1 1-1h3.5c.6 0 1 .4 1 1 0 1.3.2 2.5.6 3.6.1.3 0 .7-.2 1z"/></svg>
    1300 555 019
  </div>
  <div class="abs footer-mail">talent@vantisgroup.com.au</div>
</section>

<section class="flyer flyer--structure">
  <div class="abs photo structure-photo" role="img" aria-label="Photo of apprentices working together on an engineering rig in a workshop"></div>
  <div class="abs brand-band structure-brand"><span class="mark"></span>Vantis Group</div>
  <div class="abs pill structure-pill">COURSE STRUCTURE</div>
  <div class="abs copy copy--center structure-copy">
    <p>The Program currently has a 4-year delivery timeline. Vantis Group Talent Solutions envisages working with each company hosting a Technology Higher Apprentice, as well as with the relevant training provider on appropriate attendance schedules that maximise benefits for students, and the workplace. Training will be conducted in the work place, as well as the off-the-job delivery at the relevant training provider's facilities.</p>
    <p>The following is an indication of the current units of study for the Victorian Program which is currently being delivered by Eastbrook University of Technology's Vocational and Higher Educational sectors.</p>
  </div>
  <h3 class="abs units-title">Units of study</h3>
  <div class="abs units-level">YEARS 1 AND 2: DIPLOMA LEVEL</div>
  <ul class="abs unit-list units-col1">
    <li>Working in Industry 4.0</li>
    <li>Perform Computations</li>
    <li>Analyse a simple electrical system circuit</li>
    <li>Implement and problem solve a PLC-based industrial control system</li>
    <li>Apply project life cycle management processes</li>
    <li>Apply principles of networking technologies for manufacturing and engineering applications</li>
    <li>Work safely with collaborative robots</li>
  </ul>
  <ul class="abs unit-list units-col2">
    <li>Use hand and power tools</li>
    <li>Apply principles of OHS in the work environment</li>
    <li>Produce components using CAD and CAM technologies</li>
    <li>Troubleshoot digital control systems</li>
    <li>Produce and manage technical documentation</li>
    <li>Use SCADA system to monitor and control an industrial process</li>
    <li>Analyse and manage Big Data in cloud-based systems</li>
    <li>Project: Commission a cyber-physical system</li>
  </ul>
  <div class="abs industry-visual" role="img" aria-label="Industry 4.0 graphic with connected smart factory icons over an engine part"></div>
  <div class="abs advanced-band"></div>
  <div class="abs advanced-level">YEARS 3 AND 4: ASSOCIATE DEGREE LEVEL</div>
  <div class="abs advanced-rows">
    <div class="row"><span>Working in Industry 4.0</span><span>Engineering skills for industry 4.0</span><span>CAD / CAM and engineering materials</span></div>
    <div class="row"><span>Industrial networking and cloud computing</span><span>Electrical systems</span><span>Digital control systems</span></div>
    <div class="row"><span>Object oriented programming: Industrial control systems</span><span>Cyber physical system integration (Major Project)</span></div>
    <div class="row"><span>Software tools for industry 4.0</span><span>Advanced digital control systems</span><span>Advanced electrical machines</span></div>
    <div class="row"><span>Predictive engineering analytics</span><span>Robotics and digital twin</span><span>Cyber security and cloud services</span></div>
  </div>
  <div class="abs footer-phone">
    <svg width="10" height="10" viewBox="0 0 24 24" aria-hidden="true"><path fill="#fff" d="M6.6 10.8a15 15 0 0 0 6.6 6.6l2.2-2.2c.3-.3.7-.4 1-.2 1.1.4 2.3.6 3.6.6.6 0 1 .4 1 1V20c0 .6-.4 1-1 1A17 17 0 0 1 3 4c0-.6.4-1 1-1h3.5c.6 0 1 .4 1 1 0 1.3.2 2.5.6 3.6.1.3 0 .7-.2 1z"/></svg>
    1300 555 019
  </div>
  <div class="abs footer-mail">talent@vantisgroup.com.au</div>
</section>

</body>
</html>
```